Home page graphic design only (NOT WEBSITE DESIGN)

I require a home page to be designed for my new website.
I DO NOT REQUIRE to build a website. We are a rug company specialising in alpaca wool. It is targeted at the high end of the market and hence the graphics of our page requires to reflect this. Our current page is as per attachment and I think it is too basic.
Updates

Target Market(s)

Extremly high net worth individuals where luxury is a requirement

Requirements
Must have
• show of style, luxury, uniqueness. Prefer having bright images.
Nice to have
• a highly sofisticated roomscape where the focus in the rug. See attachment as an example
Should not have
• Not sure

```html
<!DOCTYPE html>
<html lang="en">
<head>
<meta charset="utf-8">
<title>Laine Royale – Luxury Alpaca Rugs</title>
<link rel="stylesheet" href="https://fonts.googleapis.com/css2?family=Playfair+Display:wght@400;500&family=Playball&family=Oswald:wght@600&family=Cormorant+Garamond:wght@500&display=swap">
<style>
  :root{
    --black:#000000;
    --gold:#d8b45a;
    --gold-light:#f3dc8c;
    --gold-dark:#a9822e;
    --gold-faint:#2a2418;
    --ink:#111111;
    --panel-white:rgba(255,255,255,0.55);
    --rug-light:#e6cba6;
    --rug-mid:#c9a47a;
    --room-green:#3d4a2a;
    --room-dark:#2a2a2a;
  }
  *{margin:0;padding:0;box-sizing:border-box}
  html,body{width:1200px;height:702px;overflow:hidden;background:var(--black)}
  .canvas{position:relative;width:1200px;height:702px;background:var(--black);overflow:hidden}
  .top-band,.bottom-band{position:absolute;left:0;width:1200px;background:var(--black)}
  .top-band{top:0;height:58px}
  .bottom-band{bottom:0;height:40px}
  .band-brand{position:absolute;font-family:"Playfair Display",serif;letter-spacing:1px;white-space:nowrap}
  .band-brand--left{left:20px;top:14px;font-size:24px;color:var(--gold)}
  .band-brand--right{right:22px;top:14px;font-size:24px;color:var(--gold-faint)}
  .band-brand--bottom{left:798px;top:4px;font-size:26px;color:var(--gold-faint)}

  .intro-panel{position:absolute;left:0;top:58px;width:672px;height:604px;
    background:linear-gradient(180deg,#4a4a3c 0%,#5b6a3c 14%,#8a8468 28%,#d8c2a2 40%,#e9d5b8 60%,#e2c9a5 80%,#cfb590 100%)}
  .intro-glow{position:absolute;inset:0;background:radial-gradient(ellipse at 50% 55%,rgba(255,250,240,0.55),rgba(255,250,240,0) 70%)}
  .intro-title{position:absolute;left:0;width:672px;top:88px;text-align:center;
    font-family:"Playfair Display",serif;font-weight:400;font-size:74px;letter-spacing:5px;
    transform:scaleX(0.86);color:var(--gold);
    background:linear-gradient(180deg,var(--gold-light),var(--gold) 55%,var(--gold-dark));
    -webkit-background-clip:text;background-clip:text;-webkit-text-fill-color:transparent}
  .intro-tagline{position:absolute;left:0;width:672px;top:242px;text-align:center;
    font-family:"Playball",cursive;font-size:30px;line-height:46px;color:var(--ink)}
  .intro-tagline strong{font-size:34px;font-weight:400}
  .info-box{position:absolute;left:82px;top:420px;width:506px;height:144px;background:var(--panel-white);text-align:center}
  .info-established{margin-top:14px;font-family:"Cormorant Garamond",serif;font-size:24px;letter-spacing:1px;color:var(--ink)}
  .info-regions{margin-top:4px;font-family:"Oswald",sans-serif;font-weight:600;font-size:25px;letter-spacing:0.5px;color:var(--ink)}
  .info-company{margin-top:6px;font-family:"Cormorant Garamond",serif;font-size:19px;line-height:21px;letter-spacing:1px;color:var(--ink)}

  .showroom{position:absolute;left:674px;top:58px;width:526px;height:604px}
  .showroom-photo{position:absolute;inset:0;
    background:linear-gradient(180deg,#d9d9d4 0%,#bcbcb4 18%,#3f5a2c 30%,#6a5a44 42%,#2e2e2e 50%,#d2b48e 60%,#c9a57c 80%,#343a44 92%,#2a2f38 100%)}
  .showroom-brand{position:absolute;left:216px;top:110px;width:140px;text-align:center;
    font-family:"Playfair Display",serif;font-size:20px;line-height:22px;color:var(--gold)}
</style>
</head>
<body>
<main class="canvas">
  <header class="top-band">
    <span class="band-brand band-brand--left">LAINE ROYALE</span>
    <span class="band-brand band-brand--right">LAINE ROYALE</span>
  </header>

  <section class="intro-panel">
    <div class="intro-glow" role="img" aria-label="Soft blurred view of an alpaca rug in a green-toned room"></div>
    <h1 class="intro-title">LAINE ROYALE</h1>
    <p class="intro-tagline"><strong>Exquisite</strong> luxury carpeting and area rugs made<br>from pure <strong>Peruvian Alpaca</strong></p>
    <div class="info-box">
      <p class="info-established">ESTABLISHED IN 1988</p>
      <p class="info-regions">AUSTRALIA - USA - EUROPE - UK - ASIA - UAE</p>
      <p class="info-company">LAINE ROYALE PTY LTD<br>ABN 58 214 903 117</p>
    </div>
  </section>

  <section class="showroom">
    <div class="showroom-photo" role="img" aria-label="Room with a green velvet wingback chair, potted plants and a large patchwork alpaca fur rug on a dark wooden floor"></div>
    <p class="showroom-brand">LAINE<br>ROYALE</p>
  </section>

  <footer class="bottom-band">
    <span class="band-brand band-brand--bottom">LAINE ROYALE</span>
  </footer>
</main>
</body>
</html>
```